Web Design Project

Hi everyone

Thanks for taking the time to read about this project.

Website needed for Corvel, female singer/songwriter and performer who is launching her debut album this year. She writes and performs folk/pop/soft rock music and plays guitar and piano.

see vidrelay links for examples of Corvel's style:
http://www.vidrelay.example/watch?v=Qp3TzL8wRn2
http://www.vidrelay.example/watch?v=Hk7DbVu4sYe

Looking for a classy, modern feel to the website. Cool colours are preferred but open to ideas. It needs it to have CoinTrove set up so items can be purchased from the site. The theme will be continued to Friendspace and business cards.

Examples include:

http://www.belindacrosshaw.example/

http://tessavorlund.example/

http://www.juneqtunes.example/home

Pages and content to be included:

HOME - main picture and general content

BIO - written content about Corvel

NEWS - this will be regularly updated, blog style

GIGS - this will be regularly updated

GALLERY - content will be photos only

SEE AND HEAR - content will be Videos and audios

STORE - this will have a cointrove function for purchase of CD and merchandise

GENEROSITY - this page will be devoted to charity work and updated regularly

CONTACT - information on how to contact Corvel's management

Buttons will need to provide links to VidRelay, Chirpline, Friendspace, Snapwell

I will work closely with the designers in giving feedback as ideas are generated and then provide further content such as photos and videos.

Thanks for considering this project!
Updates

HI everyone thanks for all your submissions so far. Please note the following:

- photos have been uploaded to assist with themes

- background could be a solid colour or texture (e.g. tree trunk texture)

- please use a hand writing font similar to Fontaro font "Lift Our Voice" - doesn't have to be exactly this but similar

Thank you,

Corvel

Hi again everyone

I apologise but the pixel bazaar website won't allow me to upload files. I will attempt to correct this as soon as possible. Thanks                                   

Target Market(s)

18-55 year olds who appreciate this genre of music; gay and lesbian community

Industry/Entity Type

Charity

Requirements
Should not have
• No flowers or flowery themes

```html
<!DOCTYPE html>
<html lang="en">
<head>
<meta charset="utf-8">
<title>Corvel — Official Website</title>
<link rel="stylesheet" href="https://fonts.googleapis.com/css2?family=Caveat:wght@500;700&family=Open+Sans:wght@400;600;700&display=swap">
<style>
:root{
  --page:#262626;
  --panel:#1c1c1c;
  --panel-edge:#3a3a3a;
  --blue:#19a7dc;
  --blue-dark:#0c7fae;
  --text:#d8d8d8;
  --muted:#8a8a8a;
  --ink:#111;
  --white:#fff;
}
*{box-sizing:border-box;margin:0;padding:0}
html,body{width:795px;height:1200px;overflow:hidden}
body{background:var(--page);font-family:'Open Sans',sans-serif;color:var(--text);font-size:11px}
.site{width:795px;height:1200px;position:relative;background:linear-gradient(#2e2e2e,#1f1f1f)}

/* header */
.header{height:78px;padding:22px 40px 0}
.brand{font-family:'Open Sans',sans-serif;font-weight:600;font-size:28px;color:var(--white);line-height:1}
.navbar{position:absolute;top:80px;left:36px;right:36px;height:24px;background:#3a3a3a;display:flex;align-items:center}
.nav{display:flex;list-style:none;height:100%}
.nav li{padding:0 12px;line-height:24px;font-size:10px;color:var(--text)}
.nav li.active{background:var(--blue);color:var(--white)}
.social{margin-left:auto;display:flex;gap:6px;padding-right:4px}
.social span{font-size:9px;font-weight:600;color:var(--white);padding:2px 5px;background:var(--blue-dark)}

/* hero */
.hero{position:absolute;top:106px;left:36px;right:36px;height:350px;overflow:hidden}
.hero-photo{position:absolute;inset:0;background:radial-gradient(ellipse at 38% 40%,#8a6a3e 0%,#4a3520 35%,#1a130b 70%,#0c0906 100%)}
.welcome{position:absolute;left:24px;bottom:16px;width:440px}
.welcome .hi{font-family:'Caveat',cursive;font-size:18px;color:var(--white)}
.welcome h1{font-family:'Caveat',cursive;font-weight:500;font-size:28px;color:var(--white);line-height:1}
.welcome h1 span{color:var(--blue)}
.welcome p{font-family:'Caveat',cursive;font-size:14px;color:#e6e6e6;line-height:1.15;margin-top:4px}
.side{position:absolute;top:14px;right:10px;width:160px}
.side-head{background:var(--blue);color:var(--white);font-family:'Caveat',cursive;font-size:21px;text-align:center;line-height:26px}
.show{background:#0d0d0d;text-align:center;padding:6px 6px 8px}
.show .date{font-family:'Caveat',cursive;font-size:26px;color:var(--white);line-height:1}
.show .place{font-family:'Caveat',cursive;font-size:16px;color:var(--text)}
.show a{display:block;font-family:'Caveat',cursive;font-size:14px;color:var(--blue);text-decoration:underline;margin-top:2px}
.tweet{background:#0d0d0d;padding:8px;font-size:8px;line-height:1.3;color:var(--text);text-align:center}
.tweet a{color:var(--blue);word-break:break-all}
.side .side-head.second{margin-top:10px}

/* tabs */
.tabs{position:absolute;top:460px;left:36px;right:36px;height:30px;display:flex;border-bottom:1px solid var(--panel-edge)}
.tab{font-family:'Caveat',cursive;font-size:22px;color:var(--blue);padding:0 26px;line-height:30px}
.tab.active{color:var(--white);background:var(--panel);border:1px solid var(--panel-edge);border-bottom:none}
.videos{position:absolute;top:492px;left:36px;right:36px;height:302px;background:var(--panel);padding:14px 18px}
.view-all{position:absolute;top:8px;right:18px;color:var(--blue);font-size:9px;text-decoration:underline}
.video-row{display:flex;gap:38px;margin-top:12px}
.video{width:315px}
.player{height:200px;position:relative;background:var(--ink);border:1px solid #333}
.still{position:absolute;inset:0 0 14px 0;background:radial-gradient(ellipse at 45% 45%,#8e8e8e 0%,#4a4a4a 45%,#151515 90%)}
.player-blank .title{position:absolute;left:0;right:0;top:42%;text-align:center;font-size:16px;color:#666}
.player-blank .title small{display:block;font-family:'Caveat',cursive;font-size:13px}
.controls{position:absolute;left:0;right:0;bottom:0;height:14px;background:#222;display:flex;align-items:center;padding:0 4px;gap:6px}
.controls .bar{flex:1;height:3px;background:#555}
.caption{font-size:8px;color:var(--muted);margin-top:5px;line-height:1.35}
.links{display:flex;justify-content:space-between;margin-top:4px;font-size:9px;color:var(--blue)}

/* events */
.events{position:absolute;top:806px;left:36px;right:36px;height:240px;background:var(--panel);padding:12px 18px}
.events h2{font-family:'Caveat',cursive;font-weight:500;font-size:26px;color:var(--white);border-bottom:1px solid var(--panel-edge);padding-bottom:4px}
.events .view-all{top:22px}
.event-row{display:flex;gap:18px;margin-top:14px}
.event{width:218px;display:flex;gap:6px}
.event-date{writing-mode:vertical-rl;transform:rotate(180deg);font-family:'Caveat',cursive;font-size:24px;color:var(--blue);text-align:center;width:28px}
.event-body{flex:1}
.event-photo{height:96px;border:3px solid var(--white);background:linear-gradient(135deg,#cfcfcf,#6a6a6a 60%,#2a2a2a)}
.event-body h3{font-size:10px;font-weight:600;color:var(--text);margin-top:8px}
.event-body .city{font-size:9px;color:var(--blue);font-weight:600}
.event-body .rule{height:1px;background:var(--panel-edge);margin:6px 0}
.event-body .status{font-size:9px;color:var(--blue)}

/* footer */
.footer{position:absolute;top:1062px;left:36px;right:36px;display:flex;justify-content:space-between;font-size:9px;color:var(--blue);border-top:1px solid var(--panel-edge);padding-top:10px}
.footer .legal{color:var(--text)}
</style>
</head>
<body>
<div class="site">
  <header class="header"><div class="brand">Corvel</div></header>

  <nav class="navbar">
    <ul class="nav">
      <li class="active">Home</li><li>Bio</li><li>News</li><li>Gigs</li><li>Gallery</li><li>See &amp; Hear</li><li>Store</li><li>Generosity</li><li>Contact</li>
    </ul>
    <div class="social"><span>Friendspace</span><span>Chirpline</span><span>VidRelay</span></div>
  </nav>

  <section class="hero">
    <div class="hero-photo" role="img" aria-label="Portrait of Corvel singing, warm lighting"></div>
    <div class="welcome">
      <div class="hi">Welcome to</div>
      <h1>Official Website of <span>Corvel</span></h1>
      <p>Female singer, Songwriter and Performer who is launching her debut album this year. She writes and performs folk/pop/soft rock music and plays guitar and piano.</p>
    </div>
    <aside class="side">
      <div class="side-head">Next Show</div>
      <div class="show">
        <div class="date">30 may 2013</div>
        <div class="place">Hyderabad, India</div>
        <a>View All Shows</a>
      </div>
      <div class="side-head second">Tweet</div>
      <div class="tweet">writes and performs folk/pop/soft rock music and plays guitar and piano.<br><br><a>http://www.vidrelay.example/watch?v=Qp3TzL8wRn2</a></div>
    </aside>
  </section>

  <div class="tabs">
    <div class="tab active">Latest Video</div>
    <div class="tab">Photos</div>
    <div class="tab">Latest Posts</div>
  </div>

  <section class="videos">
    <a class="view-all">View All Videos</a>
    <div class="video-row">
      <div class="video">
        <div class="player">
          <div class="still" role="img" aria-label="Video still of Corvel playing acoustic guitar"></div>
          <div class="controls"><svg width="8" height="8"><polygon points="0,0 8,4 0,8" fill="#ccc"/></svg><div class="bar"></div></div>
        </div>
        <div class="caption">Corvel Ashdane - Dark Satin (cover)<br>Published on Jan 9, 2013</div>
        <div class="links"><span>Share</span><span>Comments</span></div>
      </div>
      <div class="video">
        <div class="player player-blank">
          <div class="title">Corvel Ashdane<small>The way you lift me up</small></div>
          <div class="controls"><svg width="8" height="8"><polygon points="0,0 8,4 0,8" fill="#ccc"/></svg><div class="bar"></div></div>
        </div>
        <div class="caption">The way you lift me up (cover)<br>Published on Mar 1, 2013</div>
        <div class="links"><span>Share</span><span>Comments</span></div>
      </div>
    </div>
  </section>

  <section class="events">
    <h2>Upcoming Event</h2>
    <a class="view-all">View All Show</a>
    <div class="event-row">
      <div class="event">
        <div class="event-date">30 May 2013</div>
        <div class="event-body">
          <div class="event-photo" role="img" aria-label="Photo of Corvel with guitar"></div>
          <h3>Dark Satin</h3><div class="city">New York, NY</div><div class="rule"></div><div class="status">Sold Out</div>
        </div>
      </div>
      <div class="event">
        <div class="event-date">30 May 2013</div>
        <div class="event-body">
          <div class="event-photo" role="img" aria-label="Photo of Corvel with guitar"></div>
          <h3>Dark Satin</h3><div class="city">New York, NY</div><div class="rule"></div><div class="status">Sold Out</div>
        </div>
      </div>
      <div class="event">
        <div class="event-date">30 May 2013</div>
        <div class="event-body">
          <div class="event-photo" role="img" aria-label="Photo of Corvel with guitar"></div>
          <h3>Dark Satin</h3><div class="city">New York, NY</div><div class="rule"></div><div class="status">Buy</div>
        </div>
      </div>
    </div>
  </section>

  <footer class="footer">
    <span>© Copyright Corvel All Rights Reserved.</span>
    <span class="legal">Feedback | Privacy Policy | Terms And Condition</span>
  </footer>
</div>
</body>
</html>
```